Marlow Realty Real Estate Brokerage Recruiting Flyer

We are a real estate brokerage looking to hire more real estate agents. We need to list everything we have to offer as a company so real estate agents will join our company. this is our company website: www.Marlowrealty.example .

100% COMMISSION NO MONTHLY FEE
$450 Flat Transaction FEE

What We Offer:
24/7 Office Access
Free E & O Insurance for 1st Year
Free Online CE and PLE
Free 1,000 Business Cards
Free Professional Social Media Marketing
Free Printing, Scanning, and Copies
Free Buyer and Seller Presentation Packages
Free Filquay Cloud Based Document Management Access
Access to our Internal Brokerage Forum
Company Profit Sharing!
Private Offices Available to Rent

*Lead Generation Software with over 3,000 Leads
*10 Leads to Start
* Free Personal CRM and Website
*Restrictions and Rules apply

Company Address:
4817 Amberfield Road
Suite 512
Fairfax, VA 22194
Phone: 703-555-0147
email: info@marlowrealty.example

Target Market(s)

Real Estate Agents

Industry/Entity Type

Real Estate

Colors
0555a3
ffffff

Requirements
Must have
• 100% COMMISSION NO MONTHLY FEE
$450 Flat Transaction FEE

What We Offer:
24/7 Office Access
Free Online CE and PLE
Free 1,000 Business Cards
Company Profit Sharing!

*10 Leads to Start

Company Address:
4817 Amberfield Road
Suite 512
Fairfax, VA 22194
Phone: 703-555-0147

```html
<!DOCTYPE html>
<html lang="en">
<head>
<meta charset="utf-8">
<title>Marlow Realty – Join Our Team</title>
<link href="https://fonts.googleapis.com/css2?family=Jost:wght@300;400;500;600;700&family=Oswald:wght@500;600&display=swap" rel="stylesheet">
<style>
  :root {
    --navy: #223a78;
    --navy-deep: #1b3069;
    --navy-light: #3a5aa8;
    --white: #ffffff;
    --grey-band: #d9d9d9;
    --ink: #222222;
    --stage: #5f6b69;
  }
  * { margin: 0; padding: 0; box-sizing: border-box; }
  html, body { width: 1200px; height: 2400px; overflow: hidden; background: var(--stage); }
  .flyer {
    position: absolute; left: 0; top: 423px; width: 1200px; height: 1554px;
    background: var(--white); overflow: hidden;
    font-family: "Jost", Arial, sans-serif; color: var(--ink);
  }
  .skyline-art {
    position: absolute; left: 0; top: 240px; width: 1200px; height: 700px;
    background: linear-gradient(180deg, var(--navy-light) 0%, var(--navy) 45%, var(--navy-deep) 100%);
  }
  .brand {
    position: absolute; right: 60px; top: 95px;
    display: flex; align-items: center; gap: 18px;
    font-family: "Jost", Arial, sans-serif; font-weight: 400; font-size: 60px; line-height: 1;
    color: var(--navy); letter-spacing: 1px;
  }
  .brand-mark { width: 26px; height: 26px; background: var(--navy); }
  .headline-join {
    position: absolute; left: 0; width: 1200px; top: 335px; text-align: center;
    font-weight: 300; font-size: 200px; line-height: 1; color: var(--white); letter-spacing: 2px;
  }
  .headline-team {
    position: absolute; left: 0; width: 1200px; top: 545px; text-align: center;
    font-weight: 600; font-size: 100px; line-height: 1; color: var(--white);
  }
  .offer-box {
    position: absolute; top: 672px; height: 153px;
    border: 2px dashed rgba(255,255,255,0.85); border-radius: 22px;
    display: flex; align-items: center; justify-content: center; gap: 22px; color: var(--white);
  }
  .offer-box.commission { left: 39px; width: 547px; }
  .offer-box.fee { left: 604px; width: 551px; }
  .offer-figure { font-family: "Oswald", Arial, sans-serif; font-weight: 600; font-size: 96px; line-height: 1; }
  .offer-label { font-weight: 500; font-size: 31px; line-height: 1.15; letter-spacing: 0.5px; }
  .offers-title {
    position: absolute; left: 0; width: 1200px; top: 970px; text-align: center;
    font-weight: 600; font-size: 31px; color: var(--navy); letter-spacing: 0.5px;
  }
  .offers-rule { position: absolute; left: 280px; width: 644px; top: 1019px; height: 2px; background: #c9c9c9; }
  .offer-item {
    position: absolute; display: flex; align-items: center; gap: 12px;
    transform: translateY(-50%); font-size: 21px; line-height: 1.15; font-weight: 400; color: var(--ink);
  }
  .offer-item svg { flex: none; }
  .contact-band {
    position: absolute; left: 0; top: 1338px; width: 1200px; height: 137px; background: var(--navy); color: var(--white);
  }
  .call-label { position: absolute; left: 39px; top: 22px; font-weight: 500; font-size: 24px; letter-spacing: 0.5px; }
  .call-number { position: absolute; left: 37px; top: 54px; font-family: "Oswald", Arial, sans-serif; font-weight: 600; font-size: 64px; line-height: 1; }
  .band-divider { position: absolute; left: 457px; top: 22px; width: 3px; height: 97px; background: var(--white); }
  .perk { position: absolute; display: flex; gap: 6px; font-size: 20px; line-height: 1.15; font-weight: 400; }
  .perk svg { flex: none; margin-top: 2px; }
  .footer-band {
    position: absolute; left: 0; top: 1475px; width: 1200px; height: 79px; background: var(--grey-band);
    display: flex; align-items: center; justify-content: space-between; padding: 0 39px;
    font-size: 19px; color: var(--ink); white-space: nowrap;
  }
  .footer-band b { font-weight: 600; }
</style>
</head>
<body>
<main class="flyer">
  <div class="skyline-art" role="img" aria-label="Stylised blue city skyline illustration behind the headline"></div>

  <div class="brand"><span class="brand-mark"></span>Marlow Realty</div>

  <h1 class="headline-join">JOIN</h1>
  <h2 class="headline-team">OUR TEAM!</h2>

  <div class="offer-box commission">
    <span class="offer-figure">100%</span>
    <span class="offer-label">COMMISSION<br>NO MONTHLY FEE</span>
  </div>
  <div class="offer-box fee">
    <span class="offer-figure">$450</span>
    <span class="offer-label">FLAT<br>TRANSACTION FEE</span>
  </div>

  <h3 class="offers-title">WHAT WE OFFER</h3>
  <div class="offers-rule"></div>

  <div class="offer-item" style="left:36px;top:1068px">
    <svg width="60" height="60" viewBox="0 0 60 60"><circle cx="30" cy="30" r="27" fill="none" stroke="var(--navy)" stroke-width="2.5"/><rect x="18" y="19" width="24" height="22" rx="3" fill="var(--navy)"/><circle cx="30" cy="31" r="7" fill="#fff"/><path d="M30 27v4h3" stroke="var(--navy)" stroke-width="2" fill="none"/></svg>
    <span>24/7<br>Office Access</span>
  </div>
  <div class="offer-item" style="left:331px;top:1068px">
    <svg width="60" height="60" viewBox="0 0 60 60"><circle cx="30" cy="30" r="27" fill="none" stroke="var(--navy)" stroke-width="2.5"/><path d="M17 29a13 10 0 0 1 26 0z" fill="var(--navy)"/><path d="M30 29v8" stroke="var(--navy)" stroke-width="2.5"/><path d="M16 40q8 6 20 0" stroke="var(--navy)" stroke-width="3" fill="none"/></svg>
    <span>Free E &amp; O Insurance<br>for 1st Year</span>
  </div>
  <div class="offer-item" style="left:633px;top:1068px">
    <svg width="60" height="60" viewBox="0 0 60 60"><circle cx="30" cy="30" r="27" fill="none" stroke="var(--navy)" stroke-width="2.5"/><rect x="17" y="18" width="26" height="18" fill="var(--navy)"/><rect x="21" y="22" width="18" height="10" fill="#fff"/><rect x="24" y="38" width="12" height="3" fill="var(--navy)"/></svg>
    <span>Free Online<br>CE and PLE</span>
  </div>

  <div class="offer-item" style="left:36px;top:1175px">
    <svg width="60" height="60" viewBox="0 0 60 60"><circle cx="30" cy="30" r="27" fill="none" stroke="var(--navy)" stroke-width="2.5"/><rect x="16" y="20" width="28" height="20" rx="2" fill="var(--navy)"/><circle cx="24" cy="28" r="3" fill="#fff"/><rect x="30" y="25" width="10" height="2.5" fill="#fff"/><rect x="30" y="31" width="10" height="2.5" fill="#fff"/><rect x="20" y="34" width="8" height="2.5" fill="#fff"/></svg>
    <span>Free 1,000<br>Business Cards</span>
  </div>
  <div class="offer-item" style="left:331px;top:1175px">
    <svg width="60" height="60" viewBox="0 0 60 60"><circle cx="30" cy="30" r="27" fill="none" stroke="var(--navy)" stroke-width="2.5"/><path d="M21 21L39 39M39 21L21 39" stroke="var(--navy)" stroke-width="2.5"/><circle cx="30" cy="30" r="5" fill="var(--navy)"/><circle cx="21" cy="21" r="4" fill="var(--navy)"/><circle cx="39" cy="21" r="4" fill="var(--navy)"/><circle cx="21" cy="39" r="4" fill="var(--navy)"/><circle cx="39" cy="39" r="4" fill="var(--navy)"/></svg>
    <span>Free Professional<br>Social Media<br>Marketing</span>
  </div>
  <div class="offer-item" style="left:633px;top:1175px">
    <svg width="60" height="60" viewBox="0 0 60 60"><circle cx="30" cy="30" r="27" fill="none" stroke="var(--navy)" stroke-width="2.5"/><rect x="22" y="17" width="16" height="8" fill="var(--navy)"/><rect x="16" y="25" width="28" height="12" rx="2" fill="var(--navy)"/><rect x="22" y="33" width="16" height="10" fill="#fff" stroke="var(--navy)" stroke-width="2"/></svg>
    <span>Free Printing,<br>Scanning,and Copies</span>
  </div>
  <div class="offer-item" style="left:925px;top:1175px">
    <svg width="60" height="60" viewBox="0 0 60 60"><circle cx="30" cy="30" r="27" fill="none" stroke="var(--navy)" stroke-width="2.5"/><rect x="17" y="18" width="26" height="18" fill="var(--navy)"/><rect x="22" y="27" width="3" height="6" fill="#fff"/><rect x="28" y="23" width="3" height="10" fill="#fff"/><rect x="34" y="25" width="3" height="8" fill="#fff"/><path d="M30 36v7M25 43h10" stroke="var(--navy)" stroke-width="2.5"/></svg>
    <span>Free Buyer and<br>Seller Presentation<br>Packages</span>
  </div>

  <div class="offer-item" style="left:36px;top:1285px">
    <svg width="60" height="60" viewBox="0 0 60 60"><circle cx="30" cy="30" r="27" fill="none" stroke="var(--navy)" stroke-width="2.5"/><path d="M19 33a6 6 0 0 1 3-11 9 9 0 0 1 17 1 5 5 0 0 1 2 10z" fill="var(--navy)"/><path d="M24 35v5M30 35v7M36 35v5" stroke="var(--navy)" stroke-width="2"/></svg>
    <span>Free Filquay Cloud<br>Based Document<br>Management Access</span>
  </div>
  <div class="offer-item" style="left:331px;top:1285px">
    <svg width="60" height="60" viewBox="0 0 60 60"><circle cx="30" cy="30" r="27" fill="none" stroke="var(--navy)" stroke-width="2.5"/><circle cx="30" cy="30" r="12" fill="none" stroke="var(--navy)" stroke-width="2.5"/><path d="M18 30h24M30 18q-7 12 0 24M30 18q7 12 0 24" stroke="var(--navy)" stroke-width="2" fill="none"/></svg>
    <span>Access to our Internal<br>Brokerage Forum</span>
  </div>
  <div class="offer-item" style="left:633px;top:1285px">
    <svg width="60" height="60" viewBox="0 0 60 60"><circle cx="30" cy="30" r="27" fill="none" stroke="var(--navy)" stroke-width="2.5"/><circle cx="33" cy="24" r="7" fill="none" stroke="var(--navy)" stroke-width="2.5"/><path d="M15 36h10l8 3h10v3H30l-15-1z" fill="var(--navy)"/></svg>
    <span>Company<br>Profit Sharing!</span>
  </div>
  <div class="offer-item" style="left:925px;top:1285px">
    <svg width="60" height="60" viewBox="0 0 60 60"><circle cx="30" cy="30" r="27" fill="none" stroke="var(--navy)" stroke-width="2.5"/><circle cx="25" cy="23" r="6" fill="none" stroke="var(--navy)" stroke-width="2.5"/><path d="M29 27l6 6" stroke="var(--navy)" stroke-width="2.5"/><rect x="30" y="32" width="12" height="11" fill="var(--navy)"/></svg>
    <span>Private Offices<br>Available to Rent</span>
  </div>

  <section class="contact-band">
    <div class="call-label">CALL US TODAY!</div>
    <div class="call-number">703-555-0147</div>
    <div class="band-divider"></div>
    <div class="perk" style="left:507px;top:28px">
      <svg width="20" height="20" viewBox="0 0 20 20"><path d="M3 10l5 5 10-12" stroke="#fff" stroke-width="2.5" fill="none"/></svg>
      <span>Lead Generation Software<br>with over 3,000 Leads</span>
    </div>
    <div class="perk" style="left:507px;top:90px">
      <svg width="20" height="20" viewBox="0 0 20 20"><path d="M3 10l5 5 10-12" stroke="#fff" stroke-width="2.5" fill="none"/></svg>
      <span>10 Leads to Start</span>
    </div>
    <div class="perk" style="left:841px;top:28px">
      <svg width="20" height="20" viewBox="0 0 20 20"><path d="M3 10l5 5 10-12" stroke="#fff" stroke-width="2.5" fill="none"/></svg>
      <span>Free Personal CRM and Website</span>
    </div>
    <div class="perk" style="left:841px;top:90px">
      <svg width="20" height="20" viewBox="0 0 20 20"><path d="M3 10l5 5 10-12" stroke="#fff" stroke-width="2.5" fill="none"/></svg>
      <span>Restrictions and Rules apply</span>
    </div>
  </section>

  <footer class="footer-band">
    <span>OFFICE ADDRESS: <b>4817 Amberfield Road, Suite 512</b></span>
    <span>FAIRFAX: <b>VA 22194</b></span>
    <span>EMAIL: <b>info@marlowrealty.example</b></span>
  </footer>
</main>
</body>
</html>
```